VaultMeridan Business Card Re-Design

VaultMeridan is a specialized information security company that applies its proven methodology of security Assessment, Development, Integration and Training (A-D-I-T) to provide cyber security services in the areas of Data Protection, Network Defense and Compliance. We need the current business card re-designed to properly scale the fonts and possibly rearranging some elements (icons, lettering, etc.) to make the card more appealing to the eye. The card should have the logo that is on the web site (www.vaultmeridan-example.com). We would like ideas for both a black card (black background) and a white card (white background). We prefer rounded corners to help the card stand out but are open to all ideas. FYI: VaultMeridan's slogan is "...your security is our business".

Target Market(s)

#1 US Government Contracting Companies, #2 Commercial Companies, #3 Gen. Public.

Industry/Entity Type

Business

Contact Information for Business Card

See Description; open to the use of different fonts.

Font styles to use
Sans Serif

Colors
000000
ec1f27
ffffff

Requirements
Must have
• Company logo on web site, rounded corners, list of company offerings on the back of the card.
Nice to have
• Icons
Should not have
• none

```html
<!DOCTYPE html>
<html lang="en">
<head>
<meta charset="utf-8">
<title>VaultMeridan Business Card</title>
<link href="https://fonts.googleapis.com/css2?family=Lato:wght@400;700;900&display=swap" rel="stylesheet">
<style>
  :root {
    --stage: #3b3b3e;
    --card: #1d1e21;
    --white: #ffffff;
    --red: #ec1f27;
    --muted: #d9d9d9;
  }
  * { margin: 0; padding: 0; box-sizing: border-box; }
  html, body { width: 1200px; height: 1189px; overflow: hidden; }
  body {
    background: var(--stage);
    font-family: "Lato", sans-serif;
    color: var(--white);
    position: relative;
  }
  .card {
    position: absolute;
    width: 880px;
    height: 503px;
    background: var(--card);
    border-radius: 28px;
    box-shadow: 0 14px 30px rgba(0,0,0,.45);
    overflow: hidden;
  }
  .card--back { left: 110px; top: 58px; }
  .card--front { left: 210px; top: 628px; }

  /* Back */
  .services {
    position: absolute;
    inset: 0;
    display: flex;
    flex-direction: column;
    align-items: center;
    justify-content: center;
    padding: 0 60px;
    text-align: center;
  }
  .services__title {
    color: var(--red);
    font-weight: 900;
    font-size: 30px;
    letter-spacing: 1px;
    margin-bottom: 22px;
  }
  .services__list {
    font-size: 21px;
    line-height: 1.55;
    color: var(--white);
  }
  .services__list .sep { color: var(--red); font-weight: 700; padding: 0 4px; }
  .services__web {
    color: var(--red);
    font-size: 22px;
    font-weight: 700;
    margin-top: 34px;
    letter-spacing: .5px;
  }

  /* Front */
  .front__web {
    position: absolute;
    right: 56px;
    top: 38px;
    color: var(--red);
    font-weight: 700;
    font-size: 20px;
  }
  .brand {
    position: absolute;
    left: 62px;
    top: 74px;
  }
  .brand__name {
    display: flex;
    align-items: center;
    gap: 16px;
    font-size: 46px;
    font-weight: 400;
    letter-spacing: 3px;
    color: var(--white);
  }
  .brand__mark {
    width: 38px; height: 38px;
    background: var(--red);
  }
  .brand__tagline {
    margin: 8px 0 0 56px;
    font-size: 17px;
    color: var(--muted);
    letter-spacing: .5px;
  }
  .slogan {
    position: absolute;
    left: 62px;
    top: 194px;
    color: var(--red);
    font-size: 18px;
    letter-spacing: 5px;
    white-space: nowrap;
  }
  .person {
    position: absolute;
    right: 56px;
    top: 228px;
    text-align: right;
  }
  .person__line { display: flex; align-items: baseline; gap: 12px; justify-content: flex-end; }
  .person__name { font-weight: 900; font-size: 34px; }
  .person__bar { color: var(--red); font-size: 36px; font-weight: 700; }
  .person__title { font-size: 24px; }
  .person__creds { color: var(--red); font-size: 19px; margin-top: 2px; }
  .rule {
    position: absolute;
    left: 56px; right: 56px;
    top: 312px;
    height: 2px;
    background: var(--red);
  }
  .contacts {
    position: absolute;
    left: 56px;
    top: 330px;
    list-style: none;
  }
  .contacts li {
    display: flex;
    align-items: center;
    gap: 12px;
    font-size: 23px;
    line-height: 1.5;
  }
  .icon {
    width: 24px; height: 24px;
    background: var(--red);
    border-radius: 4px;
    display: flex; align-items: center; justify-content: center;
    flex: none;
  }
  .address {
    position: absolute;
    right: 56px;
    bottom: 56px;
    text-align: right;
    font-size: 23px;
    line-height: 1.45;
    font-style: normal;
  }
</style>
</head>
<body>

<section class="card card--back">
  <div class="services">
    <h2 class="services__title">SERVICES</h2>
    <p class="services__list">
      Secure Cloud &amp; Open Stack Solutions<span class="sep">|</span>Network Attack Penetration &amp; Defense<span class="sep">|</span>Red/Blue Team<span class="sep">|</span>Data Center Consolidation<span class="sep">|</span>Secure Virtual Computing<span class="sep">|</span>Classified Cross Domain Solutions<span class="sep">|</span>Foreign/Counter Intelligence Data Security<span class="sep">|</span>Certification &amp; Accreditation<span class="sep">|</span>Secure Wireless Solutions<span class="sep">|</span>Security Training, Assessment &amp; Integration<span class="sep">|</span>Security Subject Matter Experts<span class="sep">|</span>Executive Security Strategy Coaching<span class="sep">|</span>Data Encryption/Privacy
    </p>
    <p class="services__web">www.vaultmeridan-example.com</p>
  </div>
</section>

<section class="card card--front">
  <div class="front__web">www.vaultmeridan-example.com</div>

  <div class="brand">
    <div class="brand__name"><span class="brand__mark"></span>VaultMeridan</div>
    <div class="brand__tagline">Information Security Solutions</div>
  </div>
  <div class="slogan">...your security is our business</div>

  <div class="person">
    <div class="person__line">
      <span class="person__name">Marcus Hale</span>
      <span class="person__bar">|</span>
      <span class="person__title">President - CEO</span>
    </div>
    <div class="person__creds">CISSP, C|EH</div>
  </div>

  <div class="rule"></div>

  <ul class="contacts">
    <li>
      <span class="icon"><svg width="14" height="16" viewBox="0 0 14 16"><rect x="3" y="1" width="8" height="14" rx="1.5" fill="none" stroke="#fff" stroke-width="1.6"/><circle cx="7" cy="12.5" r="1" fill="#fff"/></svg></span>
      555.014.2290
    </li>
    <li>
      <span class="icon"><svg width="16" height="16" viewBox="0 0 16 16"><path d="M3 2h3l1 3-2 1.5a9 9 0 0 0 4.5 4.5L11 9l3 1v3a1.5 1.5 0 0 1-1.5 1.5A11.5 11.5 0 0 1 1.5 3.5 1.5 1.5 0 0 1 3 2z" fill="#fff"/></svg></span>
      555.014.7731
    </li>
    <li>
      <span class="icon"><svg width="16" height="12" viewBox="0 0 16 12"><rect x="1" y="1" width="14" height="10" fill="none" stroke="#fff" stroke-width="1.5"/><path d="M1 1l7 6 7-6M1 11l5-5M15 11l-5-5" fill="none" stroke="#fff" stroke-width="1.3"/></svg></span>
      info@vaultmeridan-example.com
    </li>
    <li>
      <span class="icon"><svg width="16" height="12" viewBox="0 0 16 12"><rect x="1" y="1" width="14" height="10" fill="none" stroke="#fff" stroke-width="1.5"/><path d="M1 1l7 6 7-6M1 11l5-5M15 11l-5-5" fill="none" stroke="#fff" stroke-width="1.3"/></svg></span>
      mhale@vaultmeridan-example.com
    </li>
  </ul>

  <address class="address">
    VaultMeridan, Inc.<br>
    2140 Harbor Ridge Rd. Suite<br>
    310 Linden, Maryland 20900
  </address>
</section>

</body>
</html>
```